Collection of baby & child print designs.

We require a collection of designs that can be edited and customised in Adobe Illustrator/InDesign so that they can be personalised for our customers.

The designs can be of anything, but must include a child's name, date of birth, or location of birth (basically any personal identifier) or a combination of the above.

A range of examples of similar products can be found here - http://qvx.zt/8Rkwp

Our designs can take influence from the examples on this site, but must be different.

We require a range of options for both boys and girls.

Reason: For amends to be made to some designs.

Target Market(s)

Parents, Friends of parents, people looking for a unique gift.

Industry/Entity Type

Baby

Requirements
Must have
• Must fit within the printable area of an A3 page.

```html
<!DOCTYPE html>
<html lang="en">
<head>
<meta charset="utf-8">
<title>Ella Rosalie – Birth Print</title>
<link rel="stylesheet" href="https://fonts.googleapis.com/css2?family=Cinzel:wght@400&family=Fredoka:wght@700&family=Fredericka+the+Great&family=Oswald:wght@700&family=Bodoni+Moda:ital,wght@1,600&display=swap">
<style>
  :root {
    --paper: #ffffff;
    --pattern-tint: #eaf5f7;
    --aqua: #a3d6dc;
    --mint: #d2e4b8;
    --lilac: #a8a3cf;
    --leaf: #7ea366;
    --slate-teal: #5b8a8c;
    --bubble-pink: #f3c3d8;
    --bubble-cream: #fbf1cf;
    --bubble-blue: #c5e7ec;
  }
  html, body {
    margin: 0;
    padding: 0;
    width: 1200px;
    height: 1005px;
    overflow: hidden;
    background: var(--paper);
  }
  .birth-print {
    display: block;
    width: 1200px;
    height: 1005px;
  }
  .heart-pattern { fill: var(--pattern-tint); }
  .first-name {
    font-family: "Cinzel", serif;
    font-size: 255px;
    fill: var(--aqua);
  }
  .middle-name {
    font-family: "Fredoka", sans-serif;
    font-weight: 700;
    font-size: 135px;
    fill: var(--mint);
  }
  .birth-day {
    font-family: "Fredericka the Great", cursive;
    font-size: 290px;
    fill: var(--lilac);
  }
  .day-suffix {
    font-family: "Oswald", sans-serif;
    font-weight: 700;
    font-size: 100px;
    fill: var(--aqua);
  }
  .birth-month {
    font-family: "Oswald", sans-serif;
    font-weight: 700;
    font-size: 178px;
    fill: var(--leaf);
  }
  .birth-year {
    font-family: "Bodoni Moda", serif;
    font-style: italic;
    font-weight: 600;
    font-size: 76px;
    fill: var(--slate-teal);
  }
  .dot-lilac { fill: var(--lilac); }
  .dot-leaf { fill: var(--leaf); }
</style>
</head>
<body>
<svg class="birth-print" viewBox="0 0 1200 1005" xmlns="http://www.w3.org/2000/svg">
  <defs>
    <linearGradient id="girl-tones" x1="0" y1="0" x2="0" y2="1">
      <stop offset="0" stop-color="#47291a"/>
      <stop offset="0.35" stop-color="#f0c67e"/>
      <stop offset="0.55" stop-color="#a3d6dc"/>
      <stop offset="1" stop-color="#f0c67e"/>
    </linearGradient>
    <linearGradient id="bubble-tones" x1="1" y1="0" x2="0" y2="1">
      <stop offset="0" stop-color="var(--bubble-pink)"/>
      <stop offset="0.5" stop-color="var(--bubble-cream)"/>
      <stop offset="1" stop-color="var(--bubble-blue)"/>
    </linearGradient>
  </defs>

  <rect class="heart-pattern" x="250" y="0" width="695" height="1005" role="img" aria-label="Faint pattern of small pale aqua hearts"/>

  <path class="bubble-spray" d="M535 700 C560 620 680 560 740 520 C770 480 790 430 800 400 L835 440 C835 520 800 600 760 660 C720 700 640 725 560 725 Z" fill="url(#bubble-tones)" role="img" aria-label="Spray of small pastel pink, cream, mint and blue bubbles"/>

  <text class="first-name" x="255" y="186" textLength="670" lengthAdjust="spacingAndGlyphs">ELLA</text>
  <text class="middle-name" x="265" y="308" textLength="670" lengthAdjust="spacingAndGlyphs">ROSALIE</text>

  <text class="birth-day" x="240" y="550" textLength="310" lengthAdjust="spacingAndGlyphs">25</text>
  <circle class="dot-lilac" cx="557" cy="535" r="23"/>
  <text class="day-suffix" x="548" y="408" textLength="62" lengthAdjust="spacingAndGlyphs">TH</text>

  <text class="birth-month" transform="translate(768 580) rotate(-90)" x="0" y="0" textLength="230" lengthAdjust="spacingAndGlyphs">JULY</text>
  <circle class="dot-leaf" cx="605" cy="565" r="17"/>

  <text class="birth-year" x="775" y="392" textLength="175" lengthAdjust="spacingAndGlyphs">2012</text>

  <rect class="girl-illustration" x="245" y="562" width="270" height="433" rx="40" fill="url(#girl-tones)" role="img" aria-label="Illustration of a curly-haired girl in a pale blue dress and red headband blowing bubbles with a green wand"/>
</svg>
</body>
</html>
```